International Sex Coach needs a Book Cover in less than 3 days

I need a cover design for my book coming out next week titled "The Open Map of Desire". The book explores the origins of our cultural ideas about sexuality and taboo and is interwoven with personal memoir.
The reader must feel that they are being pulled into an intimate sexual story, but also a deeper understanding of sex itself. Like they are jumping into bed with me, you might say. I would like the title to take up the majority of the space over an image of 3D, very real bed sheets, but I am open to your ideas. I haven't purchased any images yet, but there are a few below I was drawn to.
In its essence, this book is designed to reeducate the reader about sexuality and open them up to a new paradigm of sexual wellness.
The author name is Marisa Tolven. Page must also include the phrase: a revolutionary new approach to sexuality, relationship and love.
Size 6" x 9" (15.24 x 22.86 cm)
Thanks!
Updates

Target Market(s)

Sexually active men and women.

Industry/Entity Type

Wellness

Font styles to use
Serif

```html
<!DOCTYPE html>
<html lang="en">
<head>
<meta charset="utf-8">
<title>The Open Map of Desire — Marisa Tolven</title>
<link href="https://fonts.googleapis.com/css2?family=Bebas+Neue&display=swap" rel="stylesheet">
<style>
  :root {
    --ink-white: #ffffff;
    --accent-pink: #e8174f;
    --sheet-black: #050505;
    --sheet-shadow: #2a2a2a;
    --sheet-mid: #6f6f6f;
    --sheet-light: #c9c9c9;
    --sheet-bright: #e2e2e2;
  }
  * { margin: 0; padding: 0; box-sizing: border-box; }
  html, body {
    width: 800px;
    height: 1200px;
    overflow: hidden;
    background: var(--sheet-black);
  }
  .cover {
    position: relative;
    width: 800px;
    height: 1200px;
    overflow: hidden;
    font-family: "Bebas Neue", "Oswald", sans-serif;
    color: var(--ink-white);
    text-align: center;
  }
  .cover-photo {
    position: absolute;
    inset: 0;
    background:
      radial-gradient(ellipse 260px 180px at 560px 140px, rgba(226,226,226,0.85) 0%, rgba(226,226,226,0) 100%),
      radial-gradient(ellipse 220px 160px at 640px 420px, rgba(201,201,201,0.75) 0%, rgba(201,201,201,0) 100%),
      radial-gradient(ellipse 260px 120px at 420px 560px, rgba(170,170,170,0.55) 0%, rgba(170,170,170,0) 100%),
      radial-gradient(ellipse 200px 90px at 360px 330px, rgba(140,140,140,0.6) 0%, rgba(140,140,140,0) 100%),
      radial-gradient(ellipse 240px 260px at 690px 900px, rgba(190,190,190,0.6) 0%, rgba(190,190,190,0) 100%),
      radial-gradient(ellipse 300px 220px at 430px 860px, rgba(111,111,111,0.55) 0%, rgba(111,111,111,0) 100%),
      linear-gradient(95deg, var(--sheet-black) 0%, var(--sheet-black) 12%, var(--sheet-shadow) 26%, var(--sheet-mid) 48%, #8c8c8c 72%, #7a7a7a 100%);
  }
  .cover-shade {
    position: absolute;
    left: 0; right: 0; bottom: 0;
    height: 760px;
    background: linear-gradient(to bottom, rgba(0,0,0,0) 0%, rgba(0,0,0,0.3) 40%, rgba(0,0,0,0.5) 100%);
  }
  .author-name {
    position: absolute;
    top: 12px;
    left: 0; right: 0;
    font-size: 82px;
    line-height: 1;
    letter-spacing: 1px;
  }
  .title-lead {
    position: absolute;
    top: 678px;
    left: 0; right: 0;
    font-size: 80px;
    line-height: 1;
    letter-spacing: 1px;
  }
  .title-lead .highlight { color: var(--accent-pink); }
  .title-main {
    position: absolute;
    top: 743px;
    left: 0; right: 0;
    font-size: 305px;
    line-height: 1;
    letter-spacing: 4px;
    color: var(--accent-pink);
  }
  .tagline {
    position: absolute;
    top: 1042px;
    left: 0; right: 0;
    font-size: 48px;
    line-height: 0.95;
    letter-spacing: 4px;
  }
</style>
</head>
<body>
  <main class="cover">
    <div class="cover-photo" role="img" aria-label="Black and white photograph of a person's bare legs and feet resting on rumpled white bed sheets, lit from the right with deep shadow on the left"></div>
    <div class="cover-shade"></div>

    <p class="author-name">Marisa Tolven</p>

    <h1>
      <span class="title-lead">The <span class="highlight">Open Map</span> of</span>
      <span class="title-main">Desire</span>
    </h1>

    <p class="tagline">A revolutionary new approach to<br>sexuality, relationship and love.</p>
  </main>
</body>
</html>
```